依頼詳細
メールアドレス取得のためのランディングページのヘッダーデザインをお願いします。

キャッチコピーは以下になります。2種類ありますがまずは1つ目を作成お願いします。

ワードファイルで強調したい文字の大きさのイメージを添付(LPコピー)しますのでこれに文字の大きさのバランスを合わせたデザインをお願いします。

----------------------------------------------------------------

集客は
写真一枚で
決まる!

Webで行列ができる
魔法のランディングページ
作り方動画無料プレゼント

添付の背景デザイン(Lp1)の写真を用いてください。これよりもおすすめのデザイン画像があれば取り入れてみても構いません。

<注意点>
デザインはスマホ対応もさせるため添付(top)のようにチャッチコピーは真ん中寄せでお願いします。添付のデザインと同じくらい左と右は空白を空ける必要があります。
記載項目
集客は
写真一枚で
決まる!

Webで行列ができる
魔法のランディングページ
作り方動画無料プレゼント
サイズ
• 1600×876
希望イメージ
シンプル 複雑
単色 カラフル
暗い 明るい
日常 高級
遊び心 厳粛
未来的 伝統的
女性的 男性的
希望する色
納品ファイル
• 高解像度JPG (.jpg)
• フォトショップ形式 (.psd)
補足説明
提案数が少ないので5日間期間を延長します。

写真はあくまで背景で、文字が主役で読みやすいようにお願いします。
読みにくくなるので文字は並列に段差などつけないようにお願いします。

たくさんのご提案お待ちしています。
キャッチコピー2種類のうち2つ目はこちらでお願いします。

写真は添付のLp2を使ってください。
白文字が合いそうな気がします。

ーーーーーーーーーーーーーーー
1万人を集めた
LPの秘密を
無料で初公開!

Webで行列ができる
魔法のランディングページ
作り方動画プレゼント
ーーーーーーーーーーーーーーー
イメージに合わなかったので写真を変更することにしました。

もう一つのコピーは、添付の女性の写真でこちらの文章で作成をお願いできますでしょうか。

ーーーーーーーーーーーーーー
理想のお客様だけ
引き寄せる!
共感集客の秘密

一目であなたを好きになる
魔法のランディングページ
作り方動画プレゼント
ーーーーーーーーーーーーーー

期間を5日間延長させていいただきます。

選定確約を付けさせていただきましたのでどうぞよろしくお願いいたします。
イメージに合った提案が少ないので期間を5日間延長します。

2つの画像でのデザインは添付のようなものがイメージに近いです。
こちらをベースにご提案をいただけたら嬉しいです。

文字が大きくて読みやすいということを重要視しています。

たくさんのご提案をお待ちしています。
デザインの参考となるものを添付します。

文字に段差(高低差)をつける必要はありません。水平がよいです。

こちらのように文字が大きくて読みやすいということを意識して
いただければと思います。

シンプルなものを希望します。
■ 選んだ理由

イメージに最も近かったです。

■ 提案者全員のお礼・コメント

たくさんのご提案ありがとうございました。

```html
<!DOCTYPE html>
<html lang="ja">
<head>
<meta charset="UTF-8">
<title>魔法のランディングページ</title>
<link href="https://fonts.googleapis.com/css2?family=Kiwi+Maru:wght@400;500&family=Shippori+Mincho+B1:wght@700;800&display=swap" rel="stylesheet">
<style>
  :root {
    --ink: #111111;
    --accent-pink: #e8338a;
    --title-blue: #2aa3d6;
    --ribbon-pink: #f06aa8;
    --ribbon-deep: #d93a85;
    --frame-grey: #cfcfcf;
    --bg-white: #ffffff;
  }
  * { margin: 0; padding: 0; box-sizing: border-box; }
  html, body { width: 1200px; height: 657px; overflow: hidden; background: var(--bg-white); }
  .header {
    position: relative;
    width: 1200px;
    height: 657px;
    overflow: hidden;
    border: 2px solid var(--frame-grey);
    background:
      radial-gradient(ellipse at 50% 50%, rgba(255,255,255,0.95) 0%, rgba(255,255,255,0.7) 35%, rgba(255,255,255,0) 70%),
      linear-gradient(120deg, #ffe3f1 0%, #eaf6ff 25%, #fff7da 50%, #e4f9f0 72%, #f6e6ff 100%);
  }
  .eyebrow {
    position: absolute;
    top: 34px; left: 0; width: 100%;
    text-align: center;
    font-family: "Shippori Mincho B1", serif;
    font-weight: 800;
    font-size: 24px;
    color: var(--ink);
    letter-spacing: 1px;
  }
  .product-title {
    position: absolute;
    top: 80px; left: 0; width: 100%;
    text-align: center;
    font-family: "Shippori Mincho B1", serif;
    font-weight: 800;
    font-size: 48px;
    color: var(--title-blue);
    letter-spacing: 2px;
  }
  .photo {
    position: absolute;
    border: 4px solid #e2e2e2;
  }
  .photo--city {
    left: 70px; top: 204px; width: 182px; height: 216px;
    background: linear-gradient(180deg, #3a3a3a 0%, #8a8a8a 45%, #1c1c1c 70%, #555 100%);
  }
  .photo--people {
    left: 172px; top: 326px; width: 184px; height: 212px;
    background: linear-gradient(160deg, #e6e6e6 0%, #9a9a9a 40%, #2a2a2a 75%, #4a4a4a 100%);
  }
  .photo--portrait {
    left: 766px; top: 154px; width: 364px; height: 400px;
    border-color: var(--frame-grey);
    background: linear-gradient(135deg, #1d1a22 0%, #5a3d4a 35%, #d9a3a8 55%, #f1d2d0 70%, #3b2a33 100%);
  }
  .catch {
    position: absolute;
    left: 380px; top: 200px;
    font-family: "Kiwi Maru", serif;
    font-weight: 400;
    font-size: 84px;
    line-height: 90px;
    color: var(--ink);
    letter-spacing: 4px;
  }
  .catch .highlight { color: var(--accent-pink); }
  .ribbon {
    position: absolute;
    left: 246px; top: 550px;
    width: 704px; height: 52px;
  }
  .ribbon svg { position: absolute; inset: 0; }
  .ribbon-text {
    position: absolute; inset: 0;
    display: flex; align-items: center; justify-content: center;
    gap: 18px;
    color: #ffffff;
    font-family: "Shippori Mincho B1", serif;
    font-weight: 700;
  }
  .ribbon-text .small { font-size: 24px; }
  .ribbon-text .large { font-size: 36px; letter-spacing: 2px; }
</style>
</head>
<body>
<main class="header">
  <p class="eyebrow">Webで行列ができる</p>
  <h2 class="product-title">魔法のランディングページ</h2>

  <div class="photo photo--city" role="img" aria-label="Black and white night view of a historic city canal with buildings"></div>
  <div class="photo photo--people" role="img" aria-label="Black and white photo of two people seen from behind"></div>
  <div class="photo photo--portrait" role="img" aria-label="Fashion portrait of a woman in a fragmented collage style"></div>

  <h1 class="catch">集客は<br><span class="highlight">写</span>真一枚で<br>決まる！</h1>

  <div class="ribbon">
    <svg width="704" height="52" viewBox="0 0 704 52" aria-hidden="true">
      <defs>
        <linearGradient id="ribbonFill" x1="0" y1="0" x2="0" y2="1">
          <stop offset="0" stop-color="#f58bbd"/>
          <stop offset="1" stop-color="#e2468f"/>
        </linearGradient>
      </defs>
      <polygon points="0,0 704,0 688,26 704,52 0,52 16,26" fill="url(#ribbonFill)"/>
    </svg>
    <div class="ribbon-text">
      <span class="small">作り方動画</span>
      <span class="large">無料プレゼント</span>
    </div>
  </div>
</main>
</body>
</html>
```